Rack Card for IV Infusion Vitamin Supplement bar

We need a very eye catching rack card so that customers would instantly know it is for IV vitamin infusions. We have our previous rack card (pdf) as an example that did not bring in any clients as an example as well as another one that we did not like too much. The bar is for people to feel better with hydration and vitamins.

Target Market(s)

Anyone

Industry/Entity Type

Healthcare

Requirements
Must have
• Logo on rack card
Should not have
• Not pink other than the logo

```html
<!DOCTYPE html>
<html lang="en">
<head>
<meta charset="utf-8">
<title>Solena IV Infusion Rack Card</title>
<link href="https://fonts.googleapis.com/css2?family=Prata&family=Poppins:wght@300;500&family=Source+Serif+4:wght@400;600&family=Cutive+Mono&display=swap" rel="stylesheet">
<style>
:root{
  --green:#0d4a3b;
  --green-hi:#5f8f80;
  --beige:#e8e6da;
  --paper:#ffffff;
  --cream:#f4f2e8;
  --ink:#1d1d1d;
  --muted:#4a4a45;
  --orange:#f39a1e;
  --water:#a9c4dd;
  --bg:#c4c4c4;
  --pink:#e7739f;
}
*{margin:0;padding:0;box-sizing:border-box}
html,body{width:676px;height:1200px;overflow:hidden;background:var(--bg)}
.stage{position:relative;width:676px;height:1200px}
.card{position:absolute;top:256px;width:316px;height:687px;overflow:hidden;box-shadow:0 4px 14px rgba(0,0,0,.18)}
.card--front{left:14px;background:var(--paper)}
.card--back{left:346px;background:linear-gradient(135deg,var(--cream),#e6e3d3 60%,#f1efe4)}
.abs{position:absolute}

/* front */
.brand{left:0;width:316px;top:18px;text-align:center;color:var(--green)}
.brand__dot{display:block;width:18px;height:18px;border-radius:50%;background:var(--pink);margin:0 auto 6px}
.brand__name{font:400 21px/1 "Prata",serif;letter-spacing:5px}
.brand__sub{font:400 5px/1 "Prata",serif;letter-spacing:2.5px;margin-top:3px}
.photo{left:15px;top:105px;width:224px;height:225px;border-radius:40px 40px 0 0;background:linear-gradient(135deg,#dfe3e6,#f3f1ee 55%,#d9d6d0)}
.accent-green{left:247px;top:146px;width:60px;height:184px;border-radius:16px 0 14px 0;background:var(--green)}
.accent-beige{left:247px;top:339px;width:60px;height:61px;border-radius:14px;background:var(--beige)}
.fruit{left:15px;top:282px;width:162px;height:138px;border-radius:50%;background:radial-gradient(circle at 40% 45%,#ffc04a,var(--orange) 60%,#e07b10)}
.splash{left:175px;top:330px;width:80px;height:70px;border-radius:50%;background:radial-gradient(circle,var(--water),rgba(169,196,221,0) 70%)}
.title{left:0;width:316px;top:430px;text-align:center;font:400 28px/36px "Prata",serif;color:var(--green)}
.tagline{left:0;width:316px;top:521px;text-align:center;font:300 15px/22px "Poppins",sans-serif;color:var(--ink)}
.tagline strong{font-weight:500}
.pill-shadow{left:108px;top:628px;width:197px;height:51px;background:var(--beige);border-radius:0 0 10px 0}
.pill{left:22px;top:603px;width:272px;height:61px;border-radius:22px 0 22px 22px;background:linear-gradient(90deg,var(--green),#17594a 70%,var(--green-hi));color:#fff;text-align:center}
.pill__phone{font:400 28px/1 "Prata",serif;margin-top:9px}
.pill__web{font:400 11px/1 "Source Serif 4",serif;letter-spacing:2px;margin-top:6px}

/* back */
.band{left:17px;width:281px;height:37px;border-radius:6px;background:linear-gradient(90deg,var(--green-hi),var(--green) 45%,var(--green));color:#fff;text-align:center;font:400 18px/37px "Prata",serif}
.band--offer{top:14px}
.band--addons{top:406px}
.band--hours{top:552px;font:400 13px/37px "Source Serif 4",serif}
.col{width:132px;font:400 8.6px/11.9px "Source Serif 4",serif;color:var(--muted)}
.col--left{left:21px;top:66px}
.col--right{left:166px;top:66px}
.item{margin-bottom:11.9px}
.item__name{font-weight:600;color:var(--ink);text-transform:uppercase;letter-spacing:.2px}
.addons{font:600 8.6px/13.6px "Source Serif 4",serif;color:var(--ink)}
.addons--left{left:21px;top:462px}
.addons--right{left:178px;top:462px;color:var(--muted)}
.back-phone{left:0;width:316px;top:598px;text-align:center;font:400 28px/1 "Prata",serif;color:var(--green)}
.address{left:0;width:316px;top:640px;text-align:center;font:400 12px/15px "Cutive Mono",monospace;letter-spacing:1.5px;color:var(--ink)}
</style>
</head>
<body>
<div class="stage">

  <section class="card card--front">
    <div class="abs brand">
      <span class="brand__dot"></span>
      <div class="brand__name">SOLENA</div>
      <div class="brand__sub">HEALTH &amp; WELLNESS</div>
    </div>
    <div class="abs accent-green"></div>
    <div class="abs accent-beige"></div>
    <div class="abs photo" role="img" aria-label="Photo of a nurse placing an IV drip for a smiling client in a white robe"></div>
    <div class="abs splash" role="img" aria-label="Water splash decoration"></div>
    <div class="abs fruit" role="img" aria-label="Photo of fresh oranges with leaves"></div>
    <h1 class="abs title">IV Infusion Vitamin<br>Supplement Bar</h1>
    <p class="abs tagline"><strong>Recharge, Revitalize, &amp; Rejuvenate</strong><br>Your Body for a Healthier,<br>Happier You!</p>
    <div class="abs pill-shadow"></div>
    <div class="abs pill">
      <div class="pill__phone">555 - 210 -4870</div>
      <div class="pill__web">www.solenavitality.com</div>
    </div>
  </section>

  <section class="card card--back">
    <h2 class="abs band band--offer">What we offer?</h2>
    <div class="abs col col--left">
      <div class="item"><div class="item__name">Solena Cocktail</div>Reduce stress, fatigue, and boost your energy. Solena client favorite! (IV fluids, Vitamin C, B-complex, B12, and electrolytes)</div>
      <div class="item"><div class="item__name">Immune Support</div>Protect the immune system when risk of illness is high. Great for pre, post-travel (IV fluids, Vitamin C, B-complex, and Zinc)</div>
      <div class="item"><div class="item__name">The Glow</div>Give a glowing boost to skin and hair from inside out. (IV fluids, Glutathione, Vitamin B-complex, and Biotin)</div>
      <div class="item"><div class="item__name">NAD+ 125G/ 250G/ 500G Drip</div>Enhance your cognitive health and help reverse aging. Promotes cell regeneration. Can aid mental clarity, better sleep, and energy.</div>
    </div>
    <div class="abs col col--right">
      <div class="item"><div class="item__name">Sports Recovery</div>Recover fast from illness, exhaustion, and workouts. (IV fluids, B-complex, B12, and amino acids, and electrolytes)</div>
      <div class="item"><div class="item__name">Energized</div>Boost metabolism, burn fat easier, and feel energized. (IV fluids, B-complex, and amino acid blend)</div>
      <div class="item"><div class="item__name">Brain Power</div>Support overall brain function, increase memory recall and improve certain aspects of learning. (IV fluids, B6, alpha lipoic acid, and taurine)</div>
      <div class="item"><div class="item__name">The Jetlag Drip</div></div>
      <div class="item"><div class="item__name">The Migraine / PMS Drip</div></div>
      <div class="item"><div class="item__name">The Hangover Drip</div></div>
      <div class="item"><div class="item__name">High Dose Vitamin C</div>*Medical clearance required</div>
    </div>
    <h2 class="abs band band--addons">Infusion add-ons</h2>
    <div class="abs addons addons--left">Glutathione<br>Additional Vitamin C<br>Additional Zinc<br>Additional Magnesium<br>Anti- Inflammation Medication</div>
    <div class="abs addons addons--right">Anti-nausea Medication<br>Vitamin D Shot<br>Vitamin B12 Shot</div>
    <p class="abs band band--hours">By appointments only, including weekends</p>
    <div class="abs back-phone">555 - 210 -4870</div>
    <p class="abs address">1420 Elm Row Suite 2B<br>Ridgeford, IN 46000</p>
  </section>

</div>
</body>
</html>
```